IV Nutritional Clinic Web Design

We are working with Velmo. They are an IV Nutritional Clinic and in need of a new website design.
Some sites to use for inspiration:
https://brantlowcare.example
https://www.zolvarihealth.example
https://www.quellspa.example
https://pimrolift.example
https://www.dorvak-well.example/pages/iv-therapy-west-hollywood
https://www.tqoncowell.example/cancer-care/iv-drips/
https://drelmavita.example
https://salbrikmed.example
Thank you for taking the time to consider designing a website for us. We are web developers based in Stockton, CA, USA. Most of our projects go through the same process. Understanding this process may help you win a project with us. We custom-code all of our websites in-house. We don’t have any requirements as to what tools you use for your design, but we prefer Figma files. For any design that we label as four-stars, we send it to the client for review. The client picks the final design they want us to use. Once we complete this process, we will continue to show additional clients all the four-star sites and purchase them later. Your designs will have multiple chances to sell. For better chances of success, we ask that you follow these guidelines.
IMAGES:
If you use any images or icons in the design, we ask that you have a link to the asset so we can purchase the image/icon. Most of the designs we submit do not have the customer’s images on them unless they have some great images. Be creative; show us the feeling you are trying to portray with your image choices. Use any royalty-free site you choose. We subscribe to Corvix and mainly use their images, but we can purchase images outside of Corvix.
PLEASE NOTE: we will not submit designs to clients with watermarks on the images.
FONTS:
We ask that you identify the fonts used in the design. This can be done in a message if you want. We typically use Lumen Typeset and Corvix Fonts.
CONTENT:
We're always open to different content and ideas. We often submit designs with stock images so the client can see our vision. We typically take pictures after the website launch to use their images with our vision. Lorem Ipsum is fine for paragraphs, but we ask that you write the headers in correct English. We want to be able to show the vision and identify the sections of the website.
INSPIRATION:
We typically add a couple of links in the brief of websites we like to help you get started in your design.
REVISIONS:
We do not often ask for revisions of the designs unless we see something in the design that may not appeal to the client. If there are slight changes that we want to make, we do that in the development process.
FEEDBACK:
We rarely give feedback on designs during the design process. We are working on many website projects and do not have the time to provide feedback. We usually respond if your request is well thought out and asks specific questions, but a note asking “feedback, please” usually goes unanswered.
Number of Pages Required
1 page
Look and feel
Each slider illustrates characteristics of the customer's brand and the style your logo design should communicate.

```html
<!DOCTYPE html>
<html lang="en">
<head>
<meta charset="utf-8">
<title>Velmo Hydration – IV Nutritional Clinic</title>
<link href="https://fonts.googleapis.com/css2?family=Poppins:wght@300;400;500;600;700&display=swap" rel="stylesheet">
<style>
:root{
  --navy:#1a2580;
  --green:#74a83a;
  --ink:#22242c;
  --muted:#6b6e78;
  --soft:#f3f3f4;
  --stage:#d9d9d9;
  --footer:#20222e;
  --footer-bar:#2c2f3a;
  --white:#ffffff;
}
*{box-sizing:border-box;margin:0;padding:0}
html,body{width:1200px;height:1200px;overflow:hidden;background:var(--stage)}
body{font-family:'Poppins',sans-serif;color:var(--ink);position:relative}
.page{position:absolute;left:466px;top:0;width:1000px;height:4484px;background:var(--white);transform:scale(0.2676);transform-origin:top left;overflow:hidden}
.sec{position:absolute;left:0;width:1000px}
.abs{position:absolute}
.eyebrow{font-size:10px;font-weight:600;letter-spacing:.5px;text-transform:uppercase;color:var(--green)}
.eyebrow.dark{color:var(--ink)}
.eyebrow.light{color:var(--white)}
.h2{font-size:36px;font-weight:500;line-height:1.2;letter-spacing:-.5px}
.body{font-size:11px;line-height:1.65;color:var(--muted)}
.btn{display:inline-block;background:var(--green);color:var(--white);font-size:10px;font-weight:500;padding:7px 12px;border-radius:3px;text-transform:uppercase}
.btn.navy{background:var(--navy)}
.ticks{list-style:none}
.ticks li{font-size:11px;color:var(--muted);display:flex;align-items:center;gap:9px;margin-bottom:7px}
.ticks svg{flex:none}

/* header */
.header{top:0;height:62px}
.logo{left:29px;top:14px;display:flex;align-items:center;gap:6px;font-size:26px;font-weight:700;color:var(--navy);letter-spacing:1px}
.logo i{width:10px;height:10px;background:var(--green);display:block}
.nav{right:280px;top:22px;display:flex;gap:16px;font-size:10px;color:var(--ink);white-space:nowrap}
.socials{display:flex;gap:8px}
.header .socials{right:132px;top:17px;position:absolute}
.soc{width:26px;height:26px;border-radius:50%;background:#eef0f6}
.header .btn{position:absolute;right:29px;top:16px;padding:8px 12px;font-size:9px}

/* hero */
.hero{top:62px;left:29px;width:942px;height:500px;border-radius:12px 12px 0 0;background:linear-gradient(100deg,#d3d0d2 0%,#bdb7ba 45%,#e0dedf 75%,#cfcacb 100%)}
.hero-copy{left:78px;top:114px;width:300px}
.hero-copy h1{font-size:31px;font-weight:500;line-height:1.2;margin:8px 0 26px;letter-spacing:-.5px}
.hero-copy p{font-size:10px;color:#444;padding-bottom:16px;border-bottom:1px solid #a9a6a8;margin-bottom:16px}
.features{top:562px;left:29px;width:942px;height:152px;background:var(--navy);border-radius:0 0 12px 12px;color:var(--white)}
.feat{top:20px;width:220px}
.feat h3{font-size:12px;font-weight:500;margin:14px 0 6px}
.feat p{font-size:10px;line-height:1.6;color:#d7dbf2}

/* about */
.about{top:714px;height:526px}
.about-copy{left:105px;top:146px;width:380px}
.about-copy .h2{margin:4px 0 16px}
.about-copy .body{margin-bottom:16px}
.sign{width:170px;height:38px;margin-top:18px;background:linear-gradient(90deg,#ececee,#f6f6f7);border-radius:4px}
.ph-a{left:626px;top:81px;width:253px;height:262px;border-radius:14px;background:linear-gradient(135deg,#5f7a5c,#dfe2df 55%,#f1f1f2)}
.ph-b{left:524px;top:260px;width:181px;height:183px;border-radius:14px;background:linear-gradient(160deg,#a9b7d9,#4e78d0 55%,#e7e9ef);border:5px solid var(--white)}

/* services */
.services{top:1240px;height:412px;background:var(--soft)}
.services .eyebrow{position:absolute;left:107px;top:67px}
.services .h2{position:absolute;left:107px;top:86px;font-size:31px}
.services .btn{position:absolute;left:805px;top:91px;padding:6px 24px;font-size:8px}
.card{top:148px;height:190px;background:var(--white);border-radius:10px}
.card .ph{position:absolute;left:11px;top:10px;width:124px;height:170px;border-radius:8px}
.card h4{position:absolute;left:164px;top:45px;font-size:12px;font-weight:500}
.card p{position:absolute;left:164px;top:78px;width:120px;font-size:9px;line-height:1.6;color:var(--muted)}
.card .arr{position:absolute;right:20px;bottom:18px}

/* stats */
.stats{top:1652px;height:162px;background:var(--navy);color:var(--white)}
.stat{top:56px}
.stat b{display:block;font-size:30px;font-weight:600;line-height:1}
.stat span{font-size:9px}

/* wellness banner */
.wellness{top:1866px;left:29px;width:942px;height:500px;border-radius:12px;background:linear-gradient(100deg,#e9e9ec 0%,#d9dbe0 35%,#a8b9d2 60%,#4a79b8 80%,#e4e7ec 100%)}
.wellness-copy{left:78px;top:155px;width:220px}
.wellness-copy h2{font-size:29px;font-weight:500;line-height:1.22;margin:8px 0 24px}
.wellness-copy p{font-size:10px;color:#444;padding:14px 0;border-top:1px solid #b2b4b9;margin-bottom:4px}

/* procedure */
.procedure{top:2400px;height:600px}
.center{text-align:center;width:1000px;left:0}
.procedure .eyebrow{position:absolute;top:57px}
.procedure .h2{position:absolute;top:78px;font-size:33px}
.tab{top:160px;font-size:11px;color:var(--ink)}
.tab.on{border-bottom:1px solid var(--ink);padding-bottom:4px}
.proc-card{left:188px;top:219px;width:624px;height:295px;background:var(--soft);border-radius:14px}
.proc-card .ph{position:absolute;left:24px;top:31px;width:202px;height:238px;border-radius:10px;background:linear-gradient(160deg,#c7d4e6,#6c8fc5 55%,#2c4e8e)}
.proc-card h3{position:absolute;left:295px;top:70px;font-size:19px;font-weight:500}
.proc-card .body{position:absolute;left:295px;top:106px;width:280px;font-size:10px}
.proc-card .ticks{position:absolute;left:295px;top:178px}
.proc-card .ticks li{font-size:10px;margin-bottom:5px}

/* testimonials */
.testi{top:3017px;height:414px;background:var(--navy);color:var(--white)}
.testi-copy{left:107px;top:142px}
.testi-copy h2{font-size:33px;font-weight:500;line-height:1.15;margin:6px 0 22px}
.arrows{display:flex;gap:8px}
.arrow-btn{width:30px;height:30px;border:1px solid var(--white);border-radius:50%;display:flex;align-items:center;justify-content:center}
.quote{top:109px;width:305px;height:191px;background:var(--white);border-radius:10px;color:var(--ink);padding:20px 40px}
.quote .q{font-size:30px;color:var(--green);line-height:.6;font-weight:600;display:block;height:18px}
.quote p{font-size:9px;line-height:1.65;color:var(--muted)}
.quote h5{font-size:11px;font-weight:500;margin-top:10px}
.quote small{font-size:8px;color:var(--muted)}
.avatar{position:absolute;right:26px;bottom:18px;width:56px;height:56px;border-radius:50%;background:linear-gradient(135deg,#c7c9d0,#7c808c)}

/* news */
.news{top:3431px;height:666px}
.news .eyebrow{position:absolute;top:112px}
.news .h2{position:absolute;top:137px;font-size:33px}
.post{top:207px;width:391px;height:355px;border:2px solid var(--navy);border-radius:6px;overflow:hidden;background:var(--white)}
.post .ph{height:195px}
.date{position:absolute;right:12px;top:14px;background:var(--white);border-radius:18px;font-size:10px;padding:6px 12px}
.post h4{font-size:17px;font-weight:500;margin:48px 0 10px 33px}
.post p{font-size:9px;line-height:1.65;color:var(--muted);margin-left:33px;width:280px}

/* footer */
.footer{top:4097px;height:339px;background:var(--footer);color:var(--white)}
.fcol{top:86px}
.fcol h4{font-size:13px;font-weight:500;padding-bottom:6px;position:relative;margin-bottom:16px}
.fcol h4::after{content:"";position:absolute;left:0;bottom:0;width:30px;height:2px;background:var(--green)}
.fcol li{list-style:none;font-size:9px;color:#c9cad2;margin-bottom:9px}
.contact-line{display:flex;gap:6px;font-size:9px;color:#c9cad2;line-height:1.5;margin-bottom:6px}
.footer .soc{background:#3a3d4b;width:24px;height:24px}
.field{width:180px;height:30px;background:var(--white);border-radius:3px;font-size:8px;color:#999;padding:9px;margin:16px 0 8px}
.footer .btn{width:180px;text-align:center;font-size:8px}
.copy{top:4436px;height:48px;background:var(--footer-bar);color:#c9cad2;font-size:9px;text-align:center;line-height:48px}
.copy b{color:var(--green);font-weight:400}
</style>
</head>
<body>
<main class="page">

  <header class="sec header">
    <div class="abs logo"><i></i>Velmo</div>
    <nav class="abs nav"><span>Home</span><span>About</span><span>Services</span><span>Reviews</span><span>Blogs</span><span>Contact</span></nav>
    <div class="socials"><span class="soc"></span><span class="soc"></span><span class="soc"></span><span class="soc"></span></div>
    <span class="btn navy">Book an appointment</span>
  </header>

  <section class="abs hero" role="img" aria-label="Nurse in gloves holding an IV bag filled with sliced fruit">
    <div class="abs hero-copy">
      <div class="eyebrow dark">IV Therapy</div>
      <h1>Recharge Your Body with IV Hydration</h1>
      <p>Unlock Your Potential with IV Therapy</p>
      <span class="btn">Book an appointment</span>
    </div>
  </section>

  <section class="abs features">
    <div class="abs feat" style="left:78px">
      <svg width="30" height="26" viewBox="0 0 30 26" fill="none" stroke="#fff" stroke-width="1.4"><path d="M15 24S2 16 2 8a6.5 6.5 0 0 1 13-1 6.5 6.5 0 0 1 13 1c0 8-13 16-13 16z"/><path d="M5 13h6l2-4 3 7 2-3h7"/></svg>
      <h3>Wellness</h3><p>Lorem ipsum dolor sit amet, consectetur adipiscing elit. Ut ultricies</p>
    </div>
    <div class="abs feat" style="left:358px">
      <svg width="20" height="30" viewBox="0 0 20 30" fill="none" stroke="#fff" stroke-width="1.4"><rect x="5" y="6" width="10" height="20" rx="2"/><path d="M7 2h6v4H7zM5 13h10"/></svg>
      <h3>Hydration</h3><p>Lorem ipsum dolor sit amet, consectetur adipiscing elit. Ut ultricies</p>
    </div>
    <div class="abs feat" style="left:639px">
      <svg width="30" height="30" viewBox="0 0 30 30" fill="none" stroke="#fff" stroke-width="1.4"><path d="M3 3l8 8M11 3H3v8M27 27l-8-8M19 27h8v-8M12 18l6-6"/></svg>
      <h3>Energized</h3><p>Lorem ipsum dolor sit amet, consectetur adipiscing elit. Ut ultricies</p>
    </div>
  </section>

  <section class="sec about">
    <div class="abs about-copy">
      <div class="eyebrow">Who we are</div>
      <h2 class="h2">Boost Your Body,<br>IV Style</h2>
      <p class="body">Lorem ipsum dolor sit amet, consectetur adipiscing elit. Ut ultricies mi quis metus faucibus facilisis. Phasellus sit amet est et lacus fermentum consequat. Integer ultrices congue aliquet.</p>
      <ul class="ticks">
        <li><svg width="12" height="12" viewBox="0 0 12 12" fill="none" stroke="#74a83a"><circle cx="6" cy="6" r="5.3"/><path d="M3.5 6l1.8 1.8L8.5 4.5"/></svg>Lorem ipsum dolor sit amet,</li>
        <li><svg width="12" height="12" viewBox="0 0 12 12" fill="none" stroke="#74a83a"><circle cx="6" cy="6" r="5.3"/><path d="M3.5 6l1.8 1.8L8.5 4.5"/></svg>consectetur adipiscing elit. Ut</li>
        <li><svg width="12" height="12" viewBox="0 0 12 12" fill="none" stroke="#74a83a"><circle cx="6" cy="6" r="5.3"/><path d="M3.5 6l1.8 1.8L8.5 4.5"/></svg>ultricies mi quis metus</li>
      </ul>
      <div class="sign" role="img" aria-label="Handwritten signature of the clinic founder"></div>
    </div>
    <div class="abs ph-a" role="img" aria-label="Patient relaxing with an IV drip in a bright clinic"></div>
    <div class="abs ph-b" role="img" aria-label="Gloved hands placing an IV line on an arm"></div>
  </section>

  <section class="sec services">
    <div class="eyebrow">Our services</div>
    <h2 class="h2">Stay Hydrated, Stay Energized</h2>
    <span class="btn">View all</span>
    <div class="abs card" style="left:-210px;width:310px">
      <h4>Rejuvenate</h4><p>Lorem ipsum dolor sit amet, consectetur adipiscing elit. Ut</p>
      <svg class="arr" width="12" height="12" viewBox="0 0 12 12" fill="none" stroke="#22242c"><path d="M2 10L10 2M4 2h6v6"/></svg>
    </div>
    <div class="abs card" style="left:112px;width:310px">
      <div class="ph" role="img" aria-label="IV bag filled with fruit slices" style="background:linear-gradient(150deg,#f0a04a,#8a5c8c 50%,#7fae4a)"></div>
      <h4>Refresh Your Body</h4><p>Lorem ipsum dolor sit amet, consectetur adipiscing elit. Ut ultricies</p>
      <svg class="arr" width="12" height="12" viewBox="0 0 12 12" fill="none" stroke="#22242c"><path d="M2 10L10 2M4 2h6v6"/></svg>
    </div>
    <div class="abs card" style="left:433px;width:310px">
      <div class="ph" role="img" aria-label="Man seated during an IV session" style="background:linear-gradient(160deg,#e9e6e2,#9a8f86 55%,#3c4a6a)"></div>
      <h4>Proper Hydration</h4><p>Lorem ipsum dolor sit amet, consectetur adipiscing elit. Ut ultricies</p>
      <svg class="arr" width="12" height="12" viewBox="0 0 12 12" fill="none" stroke="#22242c"><path d="M2 10L10 2M4 2h6v6"/></svg>
    </div>
    <div class="abs card" style="left:755px;width:310px">
      <div class="ph" role="img" aria-label="Woman resting during an IV infusion" style="background:linear-gradient(160deg,#dde2e6,#a6a9ac 55%,#5f6d7c)"></div>
      <h4>IV Infusions</h4><p>Lorem ipsum dolor sit amet, consectetur adipiscing elit. Ut ultricies</p>
    </div>
  </section>

  <section class="sec stats">
    <div class="abs stat" style="left:136px"><b>858+</b><span>Satisfied Patients</span></div>
    <div class="abs stat" style="left:343px"><b>100+</b><span>Our People</span></div>
    <div class="abs stat" style="left:550px"><b>5M+</b><span>Subscriber</span></div>
    <div class="abs stat" style="left:760px"><b>1000+</b><span>Happy Clients</span></div>
  </section>

  <section class="abs wellness" role="img" aria-label="Masked nurse preparing an IV drip line">
    <div class="abs wellness-copy">
      <div class="eyebrow dark">Hydrate. Replenish. Thrive</div>
      <h2>Optimal Wellness, IV Infusion</h2>
      <p>Boost Your Energy with IV Hydration</p>
      <span class="btn">Book an appointment</span>
    </div>
  </section>

  <section class="sec procedure">
    <div class="eyebrow center">How we work</div>
    <h2 class="h2 center">Our Procedure</h2>
    <span class="abs tab on" style="left:212px">Optimal Performance</span>
    <span class="abs tab" style="left:410px">The Natural Way</span>
    <span class="abs tab" style="left:574px">IV Nutrition</span>
    <span class="abs tab" style="left:695px">Balanced Life</span>
    <div class="abs proc-card">
      <div class="ph" role="img" aria-label="Patient lying back on a clinic bed with an IV drip"></div>
      <h3>Your Wellness Partner</h3>
      <p class="body">Lorem ipsum dolor sit amet, consectetur adipiscing elit. Ut ultricies mi quis metus faucibus facilisis. Phasellus sit amet est</p>
      <ul class="ticks">
        <li><svg width="11" height="11" viewBox="0 0 12 12" fill="none" stroke="#74a83a"><circle cx="6" cy="6" r="5.3"/><path d="M3.5 6l1.8 1.8L8.5 4.5"/></svg>Lorem ipsum dolor sit amet,</li>
        <li><svg width="11" height="11" viewBox="0 0 12 12" fill="none" stroke="#74a83a"><circle cx="6" cy="6" r="5.3"/><path d="M3.5 6l1.8 1.8L8.5 4.5"/></svg>consectetur adipiscing elit. Ut ultricies</li>
        <li><svg width="11" height="11" viewBox="0 0 12 12" fill="none" stroke="#74a83a"><circle cx="6" cy="6" r="5.3"/><path d="M3.5 6l1.8 1.8L8.5 4.5"/></svg>mi quis metus faucibus facilisis.</li>
      </ul>
    </div>
  </section>

  <section class="sec testi">
    <div class="abs testi-copy">
      <div class="eyebrow light">Testimonials</div>
      <h2>What people<br>say about</h2>
      <div class="arrows">
        <span class="arrow-btn"><svg width="14" height="10" viewBox="0 0 14 10" fill="none" stroke="#fff"><path d="M13 5H1M5 1L1 5l4 4"/></svg></span>
        <span class="arrow-btn"><svg width="14" height="10" viewBox="0 0 14 10" fill="none" stroke="#fff"><path d="M1 5h12M9 1l4 4-4 4"/></svg></span>
      </div>
    </div>
    <div class="abs quote" style="left:371px">
      <span class="q">“</span>
      <p>Lorem ipsum dolor sit amet, consectetur adipiscing elit. Ut ultricies mi quis metus faucibus facilisis. Phasellus sit amet est et lacus fermentum consequat. Integer ultrices congue aliquet</p>
      <h5>Name Here</h5><small>Lorem ipsum</small>
      <span class="avatar" role="img" aria-label="Client portrait"></span>
    </div>
    <div class="abs quote" style="left:690px">
      <span class="q">“</span>
      <p>Lorem ipsum dolor sit amet, consectetur adipiscing elit. Ut ultricies mi quis metus faucibus facilisis. Phasellus sit amet est et lacus fermentum consequat. Integer ultrices congue aliquet</p>
      <h5>Name Here</h5><small>Lorem ipsum</small>
      <span class="avatar" role="img" aria-label="Client portrait"></span>
    </div>
  </section>

  <section class="sec news">
    <div class="eyebrow center">Latest post</div>
    <h2 class="h2 center">Latest news &amp; articles</h2>
    <article class="abs post" style="left:107px">
      <div class="ph" role="img" aria-label="IV bag with fruit slices held by a nurse" style="background:linear-gradient(110deg,#d6d2d3,#e8b27a 50%,#9bbf6a 70%,#dcd8d9)"></div>
      <span class="date">Feb 23, 2025</span>
      <h4>Empower Health with IV Infusions</h4>
      <p>Lorem ipsum dolor sit amet, consectetur adipiscing elit. Ut ultricies mi quis metus faucibus facilisis. Phasellus sit amet est</p>
    </article>
    <article class="abs post" style="left:505px">
      <div class="ph" role="img" aria-label="Patient resting in a white clinic chair with an IV line" style="background:linear-gradient(120deg,#e4e6ea,#c9ccd2 50%,#f1f2f4)"></div>
      <span class="date">Feb 23, 2025</span>
      <h4>Stay Hydrated, Stay Strong</h4>
      <p>Lorem ipsum dolor sit amet, consectetur adipiscing elit. Ut ultricies mi quis metus faucibus facilisis. Phasellus sit amet est</p>
    </article>
  </section>

  <footer class="sec footer">
    <div class="abs fcol" style="left:83px">
      <h4>Contact Details</h4>
      <div class="contact-line"><svg width="9" height="11" viewBox="0 0 9 11" fill="none" stroke="#74a83a"><path d="M4.5 10S1 6.5 1 4a3.5 3.5 0 0 1 7 0c0 2.5-3.5 6-3.5 6z"/><circle cx="4.5" cy="4" r="1.2"/></svg><span>Velmo Hydration<br>418 Larkmoor Ave, Fenwick, CO<br>80010</span></div>
      <div class="contact-line"><svg width="10" height="10" viewBox="0 0 10 10" fill="none" stroke="#74a83a"><path d="M2 1h2l1 2.5-1.3.8a5 5 0 0 0 2 2l.8-1.3L9 6v2a1 1 0 0 1-1 1A7 7 0 0 1 1 2a1 1 0 0 1 1-1z"/></svg><span>Call us at 555 014 2291</span></div>
      <div class="socials" style="margin-top:16px"><span class="soc"></span><span class="soc"></span><span class="soc"></span><span class="soc"></span></div>
    </div>
    <div class="abs fcol" style="left:314px"><h4>Pages</h4><ul><li>Home</li><li>About</li><li>Services</li><li>Reviews</li><li>Blogs</li><li>Contact</li></ul></div>
    <div class="abs fcol" style="left:419px"><h4>Categories</h4><ul><li>Appointments</li><li>Supplements</li></ul></div>
    <div class="abs fcol" style="left:557px"><h4>Popular Brands</h4><ul><li>Wellness Labs</li><li>Kestrow Nutrition</li><li>View All</li></ul></div>
    <div class="abs fcol" style="left:721px">
      <h4>Newsletter</h4>
      <ul><li>Sign up to get update news about us</li></ul>
      <div class="field">Enter Email</div>
      <span class="btn">Subscribe</span>
    </div>
  </footer>
  <div class="sec copy">Copyright © 2025 <b>Velmo Hydration</b>. All Rights Reserved.</div>

</main>
</body>
</html>
```